Lanterne architecture business cards

We are a new company based in New Zealand. We Specialize in High end Luxury Residential Architecture.

Every home is bespoke and is designed to each clients individual requirements and needs.

I like to design buildings that inspire people through light and form while offering a high level of comfort and usability.

Lines of sight, proportion and balance are fundamental to the spaces I create.
Updates

August 5th is current deadline - Today's date is the 13th of August.

Target Market(s)

New Zealanders who want a custom individual home design, typically 30-65 year old males and females

Industry/Entity Type

Architecture

Contact Information for Business Card

Director - Derek Tolson
Contact Number - 0279164073
Email - info@lanternearchitecture-example.co.nz
Webstie - www.lanternearchitecture-example.co.nz
Social Media - @lanternearchitecture

Font styles to use
Sans Serif

Requirements
Must have
• Logo (Both Sides)
Website
Email
Contact Number
Social Media

Nice to have
• Texture
Should not have
• More than 3 colours - typically I would've thought 2 would be good to match the logo.

```html
<!DOCTYPE html>
<html lang="en">
<head>
<meta charset="utf-8">
<title>Lanterne architecture business cards</title>
<link href="https://fonts.googleapis.com/css2?family=Jost:wght@400;600&display=swap" rel="stylesheet">
<style>
  :root {
    --backdrop: #999999;
    --card: #f7f7f6;
    --ink: #1c1d1f;
    --ink-soft: #5a5b5d;
    --card-shadow: rgba(0, 0, 0, 0.28);
  }
  * { box-sizing: border-box; margin: 0; padding: 0; }
  html, body {
    width: 1200px;
    height: 801px;
    overflow: hidden;
  }
  body {
    background: var(--backdrop);
    font-family: "Jost", sans-serif;
    color: var(--ink);
    display: flex;
    align-items: center;
    justify-content: center;
    gap: 40px;
  }
  .card {
    width: 500px;
    height: 306px;
    background: var(--card);
    box-shadow: 0 14px 30px var(--card-shadow);
    position: relative;
  }

  /* Front side */
  .card-front .person {
    position: absolute;
    left: 60px;
    top: 62px;
  }
  .person-name {
    font-weight: 600;
    font-size: 22px;
    line-height: 1;
    letter-spacing: 0.2px;
  }
  .person-role {
    font-size: 13px;
    color: var(--ink-soft);
    margin-top: 2px;
  }
  .contact-list {
    position: absolute;
    left: 60px;
    top: 136px;
    list-style: none;
  }
  .contact-item {
    display: flex;
    align-items: center;
    gap: 7px;
    font-size: 12.5px;
    color: var(--ink-soft);
    line-height: 1;
    margin-bottom: 7px;
  }
  .contact-icon {
    width: 11px;
    height: 11px;
    flex: none;
  }
  .social-dot {
    width: 9px;
    height: 9px;
    border-radius: 50%;
    background: var(--ink);
    flex: none;
  }
  .front-brand {
    position: absolute;
    right: 40px;
    top: 128px;
    font-size: 18px;
    font-weight: 400;
    letter-spacing: 1px;
    color: var(--ink);
    text-align: right;
    line-height: 1.2;
  }

  /* Back side */
  .card-back {
    display: flex;
    align-items: center;
    justify-content: center;
  }
  .back-brand {
    font-size: 26px;
    font-weight: 400;
    letter-spacing: 8px;
    text-transform: uppercase;
    color: var(--ink);
    text-align: center;
    line-height: 1.5;
  }
</style>
</head>
<body>

  <section class="card card-front" aria-label="Business card front">
    <div class="person">
      <p class="person-name">Derek Tolson</p>
      <p class="person-role">Director</p>
    </div>

    <ul class="contact-list">
      <li class="contact-item">
        <svg class="contact-icon" viewBox="0 0 24 24" aria-hidden="true">
          <path fill="#1c1d1f" d="M6.6 10.8a15 15 0 0 0 6.6 6.6l2.2-2.2a1 1 0 0 1 1-.25 11.4 11.4 0 0 0 3.6.57 1 1 0 0 1 1 1V20a1 1 0 0 1-1 1A17 17 0 0 1 3 4a1 1 0 0 1 1-1h3.5a1 1 0 0 1 1 1c0 1.25.2 2.45.57 3.57a1 1 0 0 1-.25 1z"/>
        </svg>
        <span>0279164073</span>
      </li>
      <li class="contact-item">
        <svg class="contact-icon" viewBox="0 0 24 24" aria-hidden="true">
          <rect x="2.5" y="5" width="19" height="14" fill="none" stroke="#1c1d1f" stroke-width="2"/>
          <path d="M2.5 5l9.5 8 9.5-8" fill="none" stroke="#1c1d1f" stroke-width="2"/>
        </svg>
        <span>info@lanternearchitecture-example.co.nz</span>
      </li>
      <li class="contact-item">
        <svg class="contact-icon" viewBox="0 0 24 24" aria-hidden="true">
          <circle cx="12" cy="12" r="9.5" fill="none" stroke="#1c1d1f" stroke-width="2"/>
          <ellipse cx="12" cy="12" rx="4" ry="9.5" fill="none" stroke="#1c1d1f" stroke-width="1.6"/>
          <path d="M2.5 12h19M4 7h16M4 17h16" stroke="#1c1d1f" stroke-width="1.6"/>
        </svg>
        <span>www.lanternearchitecture-example.co.nz</span>
      </li>
      <li class="contact-item">
        <span class="social-dot" aria-hidden="true"></span>
        <span>@lanternearchitecture</span>
      </li>
    </ul>

    <p class="front-brand">Lanterne<br>architecture</p>
  </section>

  <section class="card card-back" aria-label="Business card back">
    <p class="back-brand">Lanterne<br>architecture</p>
  </section>

</body>
</html>
```